Website for a web design agency

We are a website and marketing agency. We do website design, development, and well as Brindle and Quorvia advertising and analytics. We ourselves need a new website for our own brand. We are working on some designs in-house with our own designers, but we also wanted to see what outside designers would come up with.
We are starting off with the homepage, and here is the breakdown of the sections:
https://files.brindlework.example/sheet/d/7kqTr2VnPLwXeHsaMcY4oBfJzuGNtKdWiEh3Rx9pLmQb/view?mode=share
This doc also has many links to sites we have done, which you can take screenshots of for the portfolio section.
In terms of the "look" I am going for, I want to look high-end and very beautiful designs. I found this website that I like a lot that you can use some of the elements of, just as a starting point:
http://velmarkstudio.example/layouts/pixelbarn/html/ostrevo/index.html and here is another design option they have http://velmarkstudio.example/layouts/pixelbarn/html/ostrevo/index-4.html
I'm also uploading my logo. The logo matches the gold and black look from these websites, but I would be open to switching to another color scheme if needed.
This is the link to my very old website, which you can use for some of the dummy text, and a pic of myself. I will be taking more pics of myself:
https://theplumtreeandwillowgroup.example/
We need a homepage and a portfolio page right now, but if you are the winner, we will be hiring you to make additional pages.
Updates
More designs continue to come in even today, and I want to make sure no other designers are still submitting designs.
Target Market(s)
medium and large businesses owners, and non-profits
Number of Pages Required
1 page

```html
<!DOCTYPE html>
<html lang="en">
<head>
<meta charset="utf-8">
<title>Halvern Strategies — Website Development and Online Marketing</title>
<link href="https://fonts.googleapis.com/css2?family=Montserrat:wght@400;500;600;700&family=Poppins:wght@400;500&display=swap" rel="stylesheet">
<style>
:root{
  --gold:#f0b325;
  --black:#000;
  --panel:#0f0f0f;
  --card:#161616;
  --line:#2a2a2a;
  --white:#fff;
  --muted:#9a9a9a;
  --text:#d9d9d9;
}
*{box-sizing:border-box;margin:0;padding:0}
html,body{width:1200px;height:4988px;overflow:hidden;background:var(--black)}
body{font-family:"Poppins",sans-serif;color:var(--white);position:relative}
.section{position:absolute;left:0;width:1200px}
.abs{position:absolute}
.section-title{position:absolute;left:0;width:1200px;text-align:center;font-family:"Montserrat",sans-serif;font-weight:600;font-size:29px;color:var(--gold);letter-spacing:.5px}
.title-rule{position:absolute;left:578px;width:44px;height:3px;background:var(--gold)}
.brand{font-family:"Montserrat",sans-serif;font-weight:700;color:var(--gold);text-align:center;line-height:1}
.brand .name{display:block;letter-spacing:3px}
.brand .sub{display:block;letter-spacing:7px}

/* header */
.site-header{top:0;height:97px;background:var(--black)}
.site-header .brand{left:141px;top:22px}
.site-header .brand .name{font-size:34px}
.site-header .brand .sub{font-size:16px;margin-top:3px}
.main-nav a{position:absolute;top:40px;font-family:"Montserrat",sans-serif;font-size:13px;color:var(--white);text-decoration:none;font-weight:500}
.main-nav a.active{color:var(--gold)}
.btn{display:inline-block;background:var(--gold);color:var(--black);font-family:"Montserrat",sans-serif;font-weight:600;font-size:13px;text-decoration:none;text-align:center}
.nav-cta{position:absolute;left:918px;top:27px;width:140px;height:41px;line-height:41px;border:1px solid var(--gold)}

/* hero */
.hero{top:97px;height:531px}
.hero-photo{position:absolute;inset:0;background:linear-gradient(90deg,#8a8a8a 0%,#6e6e6e 45%,#5a5a5a 70%,#3e3e3e 100%)}
.hero-badge{left:139px;top:155px;height:48px;line-height:48px;padding:0 22px;background:var(--gold);color:#111;font-family:"Montserrat",sans-serif;font-weight:600;font-size:24px}
.hero-title{left:139px;top:215px;width:560px;font-family:"Montserrat",sans-serif;font-weight:500;font-size:39px;line-height:47px}
.hero-link{left:139px;top:373px;font-family:"Montserrat",sans-serif;font-weight:600;font-size:14px;letter-spacing:.5px}

/* what we do */
.services{top:628px;height:730px;background:var(--black)}
.lead{position:absolute;left:200px;width:800px;text-align:center;font-size:14px;line-height:25px;color:var(--text)}
.service-label{position:absolute;font-family:"Montserrat",sans-serif;font-weight:500;font-size:18px}

/* portfolio */
.portfolio{top:1358px;height:895px;background:var(--panel)}
.work-card{position:absolute;background:var(--black);border:1px solid var(--line)}
.work-shot{position:absolute;left:6px;top:6px;right:6px}
.work-name{position:absolute;left:0;right:0;text-align:center;font-family:"Montserrat",sans-serif;font-weight:500;font-size:15px}
.work-overlay{position:absolute;left:6px;top:6px;right:6px;bottom:6px;background:rgba(0,0,0,.72);text-align:center}
.view-all{position:absolute;left:496px;top:769px;width:207px;height:44px;line-height:44px;font-size:13px}

/* testimonials */
.testimonials{top:2253px;height:627px;background:var(--black)}
.quote-card{position:absolute;top:165px;width:440px;height:307px}
.quote-text{position:absolute;left:40px;top:52px;width:370px;padding-left:14px;border-left:3px solid var(--gold);font-size:13px;line-height:25px;color:var(--text)}
.avatar{position:absolute;border-radius:50%;background:linear-gradient(160deg,#c9ccd1,#5f6670)}
.quote-name{position:absolute;left:122px;top:212px;font-family:"Montserrat",sans-serif;font-weight:600;font-size:15px;color:var(--gold)}
.quote-role{position:absolute;left:122px;top:233px;font-size:12px;color:var(--muted)}
.dots{position:absolute;left:0;width:1200px;text-align:center;font-size:0}
.dots span{display:inline-block;width:12px;height:12px;border-radius:50%;background:#444;margin:0 3px}
.dots span.on{background:var(--gold)}

/* case studies */
.cases{top:2880px;height:650px;background:var(--panel)}
.case-card{position:absolute;top:160px;height:400px;background:var(--black);border:1px solid var(--line)}
.case-shot{position:absolute;left:7px;top:7px;right:7px;height:193px}
.case-title{position:absolute;left:15px;top:220px;font-family:"Montserrat",sans-serif;font-weight:600;font-size:15px}
.case-text{position:absolute;left:15px;top:250px;right:14px;font-size:12px;line-height:23px;color:var(--text)}
.case-more{position:absolute;left:15px;top:335px;font-family:"Montserrat",sans-serif;font-weight:600;font-size:12px;color:var(--gold)}

/* team */
.team{top:3530px;height:505px;background:var(--black)}
.member{position:absolute;top:170px;width:215px;height:250px;background:#0b0b0b;border:1px solid var(--line);text-align:center}
.member .avatar{left:36px;top:28px;width:143px;height:143px}
.mail-badge{position:absolute;width:30px;height:30px;border-radius:50%;background:var(--gold)}
.member-name{position:absolute;left:0;right:0;top:194px;font-family:"Montserrat",sans-serif;font-weight:600;font-size:15px}
.member-role{position:absolute;left:0;right:0;top:216px;font-size:12px;color:var(--muted)}

/* audit */
.audit{top:4035px;height:565px;background:var(--gold);color:#111}
.audit .section-title{color:#111}
.field{position:absolute;background:var(--white);font-size:12px;color:#555;padding:12px 0 0 32px}
.field svg{position:absolute;left:14px;top:13px}
.submit{position:absolute;left:525px;top:443px;width:150px;height:43px;line-height:43px;background:var(--black);color:var(--white);font-size:13px}

/* footer */
.site-footer{top:4600px;height:388px;background:var(--black)}
.foot-head{position:absolute;top:78px;font-family:"Montserrat",sans-serif;font-weight:600;font-size:16px;color:var(--gold)}
.foot-list{position:absolute;list-style:none;font-size:12px;color:var(--text)}
.foot-list li{height:32px}
.contact-item{position:absolute;left:333px;font-size:12px;line-height:18px;color:var(--text)}
.contact-item b{display:block;color:var(--white);font-weight:500}
.contact-item svg{position:absolute;left:0;top:2px}
.contact-item div{margin-left:20px}
.social{position:absolute;left:620px;font-size:12px;color:var(--text);line-height:28px}
.social i{display:inline-block;width:28px;height:28px;border:1.5px solid var(--white);border-radius:50%;vertical-align:middle;margin-right:12px}
.site-footer .brand{left:805px;top:146px}
.site-footer .brand .name{font-size:50px}
.site-footer .brand .sub{font-size:23px;margin-top:4px;letter-spacing:10px}
.copyright{position:absolute;left:0;width:1200px;top:340px;text-align:center;font-size:11px;color:var(--text);border-top:1px solid var(--line);padding-top:20px}
</style>
</head>
<body>

<header class="section site-header">
  <div class="abs brand"><span class="name">HALVERN</span><span class="sub">STRATEGIES</span></div>
  <nav class="main-nav">
    <a href="#" class="active" style="left:493px">HOME</a>
    <a href="#" style="left:570px">WHAT WE DO</a>
    <a href="#" style="left:699px">PORTFOLIO</a>
    <a href="#" style="left:815px">OUR TEAM</a>
  </nav>
  <a href="#" class="btn nav-cta">CONTACT US &#10140;</a>
</header>

<section class="section hero">
  <div class="hero-photo" role="img" aria-label="Portrait photo of the agency founder against a grey textured wall"></div>
  <div class="abs hero-badge">WE BUILD VALUE</div>
  <h1 class="abs hero-title">Enterprise Level Website Development and Online Marketing</h1>
  <div class="abs hero-link">SEE HOW WE DO IT &#10140;</div>
</section>

<section class="section services">
  <h2 class="section-title" style="top:80px">WHAT WE DO</h2>
  <p class="lead" style="top:160px">Lorem ipsum dolor sit amet, consectetuer adipiscing elit, sed diam nonummy nibh euismod tincidunt ut laoreet dolore magna aliquam erat volutpat. Ut wisi enim ad minim veniam, quis.</p>
  <svg class="abs" style="left:0;top:0" width="1200" height="730" viewBox="0 0 1200 730">
    <defs>
      <radialGradient id="hub" cx="50%" cy="50%" r="50%">
        <stop offset="0%" stop-color="#1a1608"/><stop offset="80%" stop-color="#0c0b07"/><stop offset="100%" stop-color="#3a2e0c"/>
      </radialGradient>
    </defs>
    <circle cx="600" cy="440" r="132" fill="url(#hub)" stroke="#2c250f" stroke-width="3"/>
    <circle cx="600" cy="440" r="112" fill="none" stroke="#1d1a10" stroke-width="2"/>
    <g stroke="#f0b325" stroke-width="3" fill="#f0b325">
      <line x1="483" y1="322" x2="510" y2="350"/><circle cx="510" cy="350" r="6"/>
      <line x1="717" y1="322" x2="690" y2="350"/><circle cx="690" cy="350" r="6"/>
      <line x1="437" y1="440" x2="470" y2="440"/><circle cx="470" cy="440" r="6"/>
      <line x1="763" y1="440" x2="730" y2="440"/><circle cx="730" cy="440" r="6"/>
      <line x1="483" y1="558" x2="510" y2="530"/><circle cx="510" cy="530" r="6"/>
      <line x1="717" y1="558" x2="690" y2="530"/><circle cx="690" cy="530" r="6"/>
    </g>
    <g fill="#000" stroke="#f0b325" stroke-width="9">
      <circle cx="449" cy="289" r="46"/><circle cx="749" cy="289" r="46"/>
      <circle cx="387" cy="440" r="46"/><circle cx="813" cy="440" r="46"/>
      <circle cx="449" cy="593" r="46"/><circle cx="749" cy="593" r="46"/>
    </g>
    <g fill="none" stroke="#fff" stroke-width="2.5" stroke-linecap="round" stroke-linejoin="round">
      <circle cx="449" cy="289" r="16"/><path d="M449 278v22M454 283h-7a3 3 0 0 0 0 6h4a3 3 0 0 1 0 6h-7"/>
      <rect x="731" y="272" width="36" height="34" rx="3"/><path d="M731 281h36M738 290h10M738 297h10M753 290h8v9h-8z"/>
      <rect x="370" y="426" width="32" height="28" rx="2"/><path d="M382 433l9 7-9 7z"/><path d="M404 424l6-5M406 431h7"/>
      <rect x="797" y="425" width="32" height="30" rx="2"/><path d="M802 448l8-9 6 6 4-4 5 7z"/><circle cx="819" cy="433" r="3"/>
      <circle cx="446" cy="590" r="14"/><path d="M456 600l10 10M440 594l4-5 4 3 5-6"/>
      <rect x="731" y="577" width="36" height="32" rx="3"/><path d="M731 585h36M749 603c-8-5-10-9-7-12 2-2 5-1 7 2 2-3 5-4 7-2 3 3 1 7-7 12z"/>
    </g>
    <text x="600" y="443" text-anchor="middle" font-family="Montserrat,sans-serif" font-weight="700" font-size="24" fill="#f0b325" letter-spacing="2">HALVERN</text>
    <text x="600" y="460" text-anchor="middle" font-family="Montserrat,sans-serif" font-weight="700" font-size="11" fill="#f0b325" letter-spacing="4">STRATEGIES</text>
  </svg>
  <div class="service-label" style="right:819px;top:278px">Ppc And Funnels</div>
  <div class="service-label" style="left:824px;top:278px">Websites</div>
  <div class="service-label" style="right:885px;top:429px">Video Marketing</div>
  <div class="service-label" style="left:885px;top:431px">Landing Pages</div>
  <div class="service-label" style="right:821px;top:582px">Analytics &amp; Optimization</div>
  <div class="service-label" style="left:824px;top:582px">Donation Pages</div>
</section>

<section class="section portfolio">
  <h2 class="section-title" style="top:80px">OUR PORTFOLIO</h2>
  <div class="title-rule" style="top:128px"></div>

  <div class="work-card" style="left:141px;top:167px;width:277px;height:260px">
    <div class="work-shot" role="img" aria-label="Website screenshot for Orvane Productions" style="height:203px;background:linear-gradient(180deg,#f2f2f2 0 10%,#1b3a66 10% 55%,#f4f4f4 55% 80%,#6a5a4a 80%)"></div>
    <div class="work-name" style="top:222px">Orvane Productions</div>
  </div>
  <div class="work-card" style="left:141px;top:472px;width:277px;height:257px">
    <div class="work-shot" role="img" aria-label="Website screenshot for Lintel Decor Co" style="height:200px;background:linear-gradient(180deg,#5a4030 0 52%,#f3f3f3 52%)"></div>
    <div class="work-name" style="top:220px">Lintel Decor Co</div>
  </div>
  <div class="work-card" style="left:460px;top:167px;width:275px;height:562px">
    <div class="work-shot" role="img" aria-label="Full-page website screenshot for Tamsel Hope Center" style="bottom:6px;background:linear-gradient(180deg,#e9eef6 0 20%,#c9d6e8 20% 45%,#f2f2f2 45% 70%,#dfe6ef 70%)"></div>
    <div class="work-overlay">
      <div class="work-name" style="top:210px">Tamsel Hope Center</div>
      <p style="position:absolute;left:28px;right:28px;top:238px;font-size:12px;line-height:19px;color:#ddd">Lorem ipsum dolor sit consectetuer adipiscing elit, sed diam nonummy nibh euismod tincidunt ut.</p>
      <span class="btn" style="position:absolute;left:78px;top:310px;width:118px;height:36px;line-height:36px;font-size:12px">VISIT SITE &#10140;</span>
    </div>
  </div>
  <div class="work-card" style="left:778px;top:167px;width:280px;height:260px">
    <div class="work-shot" role="img" aria-label="Website screenshot for Brevtac" style="height:203px;background:linear-gradient(135deg,#1f2d6e 0 55%,#e55a25 55%)"></div>
    <div class="work-name" style="top:222px">Brevtac</div>
  </div>
  <div class="work-card" style="left:778px;top:472px;width:280px;height:257px">
    <div class="work-shot" role="img" aria-label="Website screenshot for Marisol Venn" style="height:200px;background:linear-gradient(90deg,#fbf3ee 0 55%,#c9a48c 55%)"></div>
    <div class="work-name" style="top:220px">Marisol Venn</div>
  </div>
  <a href="#" class="btn view-all">VIEW ALL PORTFOLIO &#10140;</a>
</section>

<section class="section testimonials">
  <h2 class="section-title" style="top:80px">CLIENT TESTIMONIALS</h2>
  <div class="title-rule" style="top:128px"></div>
  <div class="quote-card" style="left:141px">
    <svg class="abs" width="440" height="340" viewBox="0 0 440 340"><path d="M1 1H439V306H40L1 338Z" fill="#000" stroke="#2a2a2a" stroke-width="2"/></svg>
    <p class="quote-text">Lorem ipsum dolor sit amet, consectetuer adipiscing elit, sed diam nonummy nibh euismod tinunt ut laoreet dolore magna aliuam erat vopat. Ut wisi enim ad minim veniam, quis nostrud exerci tation.</p>
    <div class="avatar" style="left:38px;top:200px;width:66px;height:66px" role="img" aria-label="Client portrait"></div>
    <div class="quote-name">Jhon Smith</div>
    <div class="quote-role">Lorem Ipsum</div>
  </div>
  <div class="quote-card" style="left:618px">
    <svg class="abs" width="440" height="340" viewBox="0 0 440 340"><path d="M1 1H439V306H40L1 338Z" fill="#000" stroke="#2a2a2a" stroke-width="2"/></svg>
    <p class="quote-text">Lorem ipsum dolor sit amet, consectetuer adipiscing elit, sed diam nonummy nibh euismod tinunt ut laoreet dolore magna aliuam erat vopat. Ut wisi enim ad minim veniam, quis nostrud exerci tation.</p>
    <div class="avatar" style="left:38px;top:200px;width:66px;height:66px" role="img" aria-label="Client portrait"></div>
    <div class="quote-name">Dainial Bolt</div>
    <div class="quote-role">Lorem Ipsum</div>
  </div>
  <div class="dots" style="top:530px"><span></span><span class="on"></span><span></span><span></span></div>
</section>

<section class="section cases">
  <h2 class="section-title" style="top:80px">CASE STUDIES</h2>
  <div class="title-rule" style="top:128px"></div>
  <div class="case-card" style="left:141px;width:277px">
    <div class="case-shot" role="img" aria-label="Photo of a developer working at a laptop" style="background:linear-gradient(135deg,#8d7a5a,#3b3a36)"></div>
    <div class="case-title">Lorem Ipsum Dolor Sit Consuer.</div>
    <p class="case-text">Lorem ipsum dolor sit amet consectetuer adipiscing sed diam nonhmy nibh euismod tincidunt ut laoreet dolore na.</p>
    <div class="case-more">READ MORE &#10140;</div>
  </div>
  <div class="case-card" style="left:458px;width:283px">
    <div class="case-shot" role="img" aria-label="Photo of code on dual monitors" style="background:linear-gradient(135deg,#1c2430,#0a0d12 60%,#2d4a6a)"></div>
    <div class="case-title">Lorem Ipsum Dolor Sit Consuer.</div>
    <p class="case-text">Lorem ipsum dolor sit amet consectetuer adipiscing sed diam nonhmy nibh euismod tincidunt ut laoreet dolore na.</p>
    <div class="case-more">READ MORE &#10140;</div>
  </div>
  <div class="case-card" style="left:774px;width:284px">
    <div class="case-shot" role="img" aria-label="Photo of a man working on a laptop in a café" style="background:linear-gradient(135deg,#cfc6b8,#5b6a7a)"></div>
    <div class="case-title">Lorem Ipsum Dolor Sit Consuer.</div>
    <p class="case-text">Lorem ipsum dolor sit amet consectetuer adipiscing sed diam nonhmy nibh euismod tincidunt ut laoreet dolore na.</p>
    <div class="case-more">READ MORE &#10140;</div>
  </div>
  <div class="dots" style="top:553px"><span></span><span class="on"></span><span></span><span></span></div>
</section>

<section class="section team">
  <h2 class="section-title" style="top:80px">OUR TEAM</h2>
  <div class="title-rule" style="top:128px"></div>
  <div class="member" style="left:141px">
    <div class="avatar" role="img" aria-label="Team member portrait"></div><span class="mail-badge" style="left:148px;top:132px"></span>
    <div class="member-name">JHONE DOE</div><div class="member-role">Designation</div>
  </div>
  <div class="member" style="left:375px">
    <div class="avatar" role="img" aria-label="Team member portrait"></div><span class="mail-badge" style="left:148px;top:132px"></span>
    <div class="member-name">JHONE DOE</div><div class="member-role">Designation</div>
  </div>
  <div class="member" style="left:609px">
    <div class="avatar" role="img" aria-label="Team member portrait" style="left:60px;top:26px;width:96px;height:96px"></div><span class="mail-badge" style="left:128px;top:94px"></span>
    <div class="member-name" style="top:145px">JHONE DOE</div>
    <p style="position:absolute;left:22px;right:22px;top:170px;font-size:11.5px;line-height:18px;color:#d9d9d9">Lorem ipsum dolor sit amet, consectetuer adipiscing elit, sed diam nd <span style="color:var(--gold)">READ MORE...</span></p>
  </div>
  <div class="member" style="left:843px">
    <div class="avatar" role="img" aria-label="Team member portrait"></div><span class="mail-badge" style="left:148px;top:132px"></span>
    <div class="member-name">JHONE DOE</div><div class="member-role">Designation</div>
  </div>
</section>

<section class="section audit">
  <h2 class="section-title" style="top:75px">GET A FREE AUDIT &amp; CONSULTATION</h2>
  <p class="lead" style="top:148px;left:350px;width:500px;font-size:12px;line-height:21px;color:#111">Lorem ipsum dolor sit amet, consectetuer adipiscing elit, sed diam nonummy nibh euismod tincidunt ut laoreet dolore magna aliquam erat volutpat.</p>
  <div class="abs" style="left:0;width:1200px;top:183px;text-align:center;font-size:11px">Phone</div>
  <div class="field" style="left:255px;top:223px;width:338px;height:42px"><svg width="11" height="12" viewBox="0 0 11 12"><circle cx="5.5" cy="3" r="3" fill="#f0b325"/><path d="M0 12a5.5 5 0 0 1 11 0z" fill="#f0b325"/></svg>First Name</div>
  <div class="field" style="left:607px;top:223px;width:338px;height:42px"><svg width="11" height="12" viewBox="0 0 11 12"><circle cx="5.5" cy="3" r="3" fill="#f0b325"/><path d="M0 12a5.5 5 0 0 1 11 0z" fill="#f0b325"/></svg>Last Name</div>
  <div class="field" style="left:255px;top:273px;width:338px;height:42px"><svg width="12" height="10" viewBox="0 0 12 10"><rect width="12" height="10" fill="#f0b325"/><path d="M0 0l6 5 6-5" stroke="#fff" fill="none"/></svg>Email</div>
  <div class="field" style="left:607px;top:273px;width:338px;height:42px"><svg width="11" height="11" viewBox="0 0 11 11"><path d="M2 0l2 3-1 1.5c1 2 2 3 3.5 3.5L8 7l3 2-1 2C5 11 0 6 0 1z" fill="#f0b325"/></svg>Phone</div>
  <div class="field" style="left:255px;top:326px;width:690px;height:104px"><svg width="11" height="11" viewBox="0 0 11 11"><rect width="11" height="11" rx="1" fill="#f0b325"/><path d="M3 8l1-3 4-4 2 2-4 4z" fill="#fff"/></svg>Message</div>
  <a href="#" class="btn submit">SUBMIT NOW &#10140;</a>
</section>

<footer class="section site-footer">
  <h3 class="foot-head" style="left:141px">QUICK LINKS</h3>
  <ul class="foot-list" style="left:141px;top:118px">
    <li>• Home</li><li>• What We Do</li><li>• Portfolio</li><li>• Our Team</li><li>• Contact Us</li>
  </ul>
  <h3 class="foot-head" style="left:333px">CONTACT DETAILS</h3>
  <div class="contact-item" style="top:118px"><svg width="10" height="13" viewBox="0 0 10 13"><path d="M5 13S0 7 0 5a5 5 0 0 1 10 0c0 2-5 8-5 8z" fill="#f0b325"/><circle cx="5" cy="5" r="2" fill="#000"/></svg><div><b>ADDRESS</b>123 Lorem ipsum dolor sit amet,<br>consectetuer adipiscing.</div></div>
  <div class="contact-item" style="top:182px"><svg width="11" height="11" viewBox="0 0 11 11"><path d="M2 0l2 3-1 1.5c1 2 2 3 3.5 3.5L8 7l3 2-1 2C5 11 0 6 0 1z" fill="#f0b325"/></svg><div><b>PHONE</b>123-456-7890</div></div>
  <div class="contact-item" style="top:226px"><svg width="12" height="10" viewBox="0 0 12 10"><rect width="12" height="10" fill="#f0b325"/><path d="M0 0l6 5 6-5" stroke="#000" fill="none"/></svg><div><b>EMAIL</b>info@halvernstrategies.example</div></div>
  <h3 class="foot-head" style="left:620px">FOLLOW US</h3>
  <div class="social" style="top:114px"><i></i>Quorvia</div>
  <div class="social" style="top:152px"><i></i>Lumigram</div>
  <div class="social" style="top:190px"><i></i>Chirpline</div>
  <div class="social" style="top:228px"><i></i>Vidora</div>
  <div class="abs brand"><span class="name">HALVERN</span><span class="sub">STRATEGIES</span></div>
  <p class="copyright">Copyright © 2021 Halvern Strategies. All Rights Reserved.</p>
</footer>

</body>
</html>
```